Interactive Theatre Infographic

The purpose in having this infographic is to educate our customers on how interactive theatre works.
Theatre attendees usually watch theatre and the characters never act as though they know there is an audience present.  This is known as the fourth wall.  With interactive theatre there is no fourth wall.  The audience is written into the narrative of the story.  The actors still perform scenes in a script but may require the audience to help solve problems, cast votes or on occasions audiences can find clues or make discoveries.  Each theatre event has a different design.  Within each show the audience will be taken to different locations(inside or outside) where scenes are enacted.  Actors may need to improvise their interactions with the audience.
From the audience perspective there are no lines to learn.  They do not have to get too involved.  The actors will control the interactions - the actors serve both as characters and guides.
There are three main components: the audience, the actors, and the story - all rolled into one.  A short synopis of interactive theatre works is below.
Interactive theatre – where you form part of the unfolding narrative.
Play witness to fully scripted performances in which actor led interaction means that you become involved in shaping the outcome of the story.  Where the fate of character lives may depend on the decisions you make.
Interactive theatre – where the fourth wall has been burned to the ground.  It’s just you, the characters and the story all rolled into one.
Book into a unique Silver Lantern Theatrical experience today – and maybe, just maybe, you might survive…..
Our website is www.silverlantern-example.com.au & an example of a theatre event can be seen at www.silverlantern-example.com.au/theatre/

Updates
Target Market(s)
Event customers. Theatre attendees. Age ranges wil be 18-50 most likely.
Requirements
Should not have
- Please do not use the image for our current theatre show. We need a generic design.

```html
<!DOCTYPE html>
<html lang="en">
<head>
<meta charset="utf-8">
<title>What Is An Interactive Theatre?</title>
<link rel="stylesheet" href="https://fonts.googleapis.com/css2?family=Bebas+Neue&family=Open+Sans:wght@400;600&display=swap">
<style>
:root{
  --bg:#121316;
  --ink:#ffffff;
  --orange:#f7941d;
  --blue:#00aeef;
  --grey:#5a5a5c;
  --rule:#5b5c60;
}
*{margin:0;padding:0;box-sizing:border-box}
html,body{width:849px;height:1200px;overflow:hidden;background:var(--bg)}
.infographic{position:relative;width:849px;height:1200px;background:var(--bg);color:var(--ink);font-family:"Open Sans",Arial,sans-serif}
.display{font-family:"Bebas Neue",Impact,sans-serif;font-weight:400;letter-spacing:.5px;position:absolute;left:0;width:100%;text-align:center;line-height:1}
.accent{color:var(--orange)}
.title{top:42px;font-size:64px}
.body-text{position:absolute;font-size:12.7px;line-height:15.5px;font-weight:600}
.intro{left:318px;top:143px;width:212px;text-align:center}
.intro p+p{margin-top:18px}
.no-wall{font-family:"Bebas Neue",Impact,sans-serif;font-size:24px;color:var(--orange);display:block;margin-top:2px;font-weight:400}
.stage{position:absolute;border-radius:6px}
.stage-left{left:51px;top:132px;width:263px;height:216px;background:linear-gradient(180deg,#4f4f52 0%,#3a3a3d 55%,#0f86bd 100%)}
.stage-right{left:543px;top:132px;width:251px;height:199px;background:linear-gradient(180deg,#4f4f52 0%,#3a3a3d 55%,#0f86bd 100%)}
.divider{position:absolute;left:0;width:100%;border-top:2px dashed var(--rule)}
.div-1{top:367px}
.div-2{top:776px}
.h-narrative{top:387px;font-size:25px}
.icon{position:absolute}
.crowd{position:absolute;background:var(--blue);border-radius:14px 14px 8px 8px}
.crowd-row{left:346px;top:470px;width:124px;height:72px}
.caption{left:0;width:100%;top:578px;text-align:center}
.locations{left:411px;top:675px;width:300px}
.h-unfold{top:799px;font-size:25px}
.synopsis{left:81px;top:884px;width:364px;font-size:12.7px;line-height:18.7px;text-align:justify}
.h-components{top:1052px;font-size:25px}
.book{left:0;width:100%;top:1097px;text-align:center;font-size:13.3px}
.url{top:1128px;font-size:26px;color:var(--orange)}
.feather{position:absolute;left:676px;top:852px;width:88px;height:96px;background:linear-gradient(135deg,#ffffff,#cfcfd2);border-radius:60% 10% 60% 10%}
.actors{position:absolute;left:583px;top:952px;width:98px;height:68px;background:var(--orange);border-radius:10px 10px 4px 4px}
.crowd-small{left:532px;top:877px;width:90px;height:45px}
</style>
</head>
<body>
<main class="infographic">
  <h1 class="display title">What is an <span class="accent">interactive theatre?</span></h1>

  <div class="stage stage-left" role="img" aria-label="Illustration: traditional stage with two actors performing behind a dashed fourth wall, seated audience below"></div>
  <div class="stage stage-right" role="img" aria-label="Illustration: interactive stage with an actor reaching toward the audience, some audience members highlighted"></div>

  <div class="body-text intro">
    <p>In traditional theatre the characters never act as though they know there is an audience present. This is known as the fourth wall.</p>
    <p>With interactive theatre there is <span class="no-wall">No fourth wall.</span></p>
  </div>

  <hr class="divider div-1">

  <h2 class="display h-narrative">The audience is written <span class="accent">into the narrative of the story.</span></h2>

  <svg class="icon" style="left:91px;top:462px" width="114" height="84" viewBox="0 0 114 84" aria-label="Discussion bubbles" role="img">
    <ellipse cx="32" cy="32" rx="32" ry="24" fill="var(--orange)"/>
    <path d="M14 50 L8 68 L30 54Z" fill="var(--orange)"/>
    <text x="32" y="40" text-anchor="middle" font-family="Open Sans,sans-serif" font-weight="600" font-size="20" fill="#121316">?</text>
    <ellipse cx="90" cy="18" rx="22" ry="16" fill="var(--blue)"/>
    <path d="M100 30 L108 42 L92 33Z" fill="var(--blue)"/>
    <circle cx="83" cy="18" r="2.4" fill="#121316"/><circle cx="90" cy="18" r="2.4" fill="#121316"/><circle cx="97" cy="18" r="2.4" fill="#121316"/>
    <ellipse cx="83" cy="60" rx="22" ry="17" fill="var(--blue)"/>
    <path d="M92 73 L100 84 L84 76Z" fill="var(--blue)"/>
    <text x="83" y="67" text-anchor="middle" font-family="Open Sans,sans-serif" font-weight="600" font-size="18" fill="#121316">!</text>
  </svg>

  <svg class="icon" style="left:238px;top:450px" width="66" height="88" viewBox="0 0 66 88" aria-label="Lightbulb idea" role="img">
    <g stroke="var(--orange)" stroke-width="2.5" stroke-linecap="round">
      <line x1="17" y1="4" x2="21" y2="12"/><line x1="49" y1="4" x2="45" y2="12"/>
      <line x1="3" y1="20" x2="11" y2="24"/><line x1="63" y1="20" x2="55" y2="24"/>
    </g>
    <path d="M33 26 a19 19 0 0 1 11 34 v8 h-22 v-8 a19 19 0 0 1 11 -34Z" fill="none" stroke="var(--orange)" stroke-width="5"/>
    <rect x="22" y="70" width="22" height="5" rx="2" fill="var(--orange)"/>
    <rect x="24" y="77" width="18" height="5" rx="2" fill="var(--orange)"/>
  </svg>

  <div class="crowd crowd-row" role="img" aria-label="Illustration: audience silhouettes raising hands"></div>

  <svg class="icon" style="left:494px;top:476px" width="76" height="66" viewBox="0 0 76 66" aria-label="Magnifying glass" role="img">
    <circle cx="22" cy="22" r="17" fill="none" stroke="var(--orange)" stroke-width="6"/>
    <path d="M34 35 L70 62 L74 58 L39 30Z" fill="var(--orange)"/>
  </svg>

  <svg class="icon" style="left:598px;top:474px" width="156" height="72" viewBox="0 0 156 72" aria-label="Treasure trail to an X mark" role="img">
    <path d="M4 44 C20 36 40 40 34 28 C24 8 58 0 72 14 C86 28 78 56 92 64 C104 70 118 66 120 54" fill="none" stroke="var(--blue)" stroke-width="2.5" stroke-dasharray="5 5"/>
    <g stroke="var(--orange)" stroke-width="7" stroke-linecap="round"><line x1="126" y1="24" x2="150" y2="48"/><line x1="150" y1="24" x2="126" y2="48"/></g>
  </svg>

  <p class="body-text caption">The actors may require the audience solve problems, cast votes, find clues or make discoveries</p>

  <svg class="icon" style="left:158px;top:652px" width="220" height="80" viewBox="0 0 220 80" aria-label="Route between location pins" role="img">
    <path d="M12 76 L70 66 L66 48 L114 38 M70 48 L108 68 L130 70 L196 56" fill="none" stroke="#fff" stroke-width="2.5" stroke-dasharray="6 5"/>
    <path d="M16 24 a12 12 0 0 1 24 0 c0 12 -12 26 -12 26 s-12 -14 -12 -26Z" fill="var(--orange)"/>
    <circle cx="28" cy="24" r="4.5" fill="#121316"/>
    <path d="M109 10 a9 9 0 0 1 18 0 c0 9 -9 20 -9 20 s-9 -11 -9 -20Z" fill="var(--orange)"/>
    <circle cx="118" cy="10" r="3.4" fill="#121316"/>
    <path d="M196 47 a9 9 0 0 1 18 0 c0 9 -9 20 -9 20 s-9 -11 -9 -20Z" fill="var(--blue)"/>
    <circle cx="205" cy="47" r="3.4" fill="#121316"/>
  </svg>

  <p class="body-text locations">Within each show the audience will be taken to different locations(inside or outside) where scenes are enacted.</p>

  <hr class="divider div-2">

  <h2 class="display h-unfold">Interactive theatre – <span class="accent">where you form part of the unfolding narrative.</span></h2>

  <p class="body-text synopsis">Play witness to fully scripted performances in which actor led interaction means that you become involved in shaping the outcome of the story. Where the fate of character lives may depend on the decisions you make. Where the fourth wall has been burned to the ground. It’s just you, the characters and the story all rolled into one.</p>

  <svg class="icon" style="left:558px;top:848px" width="190" height="176" viewBox="0 0 190 176" aria-hidden="true">
    <circle cx="80" cy="88" r="80" fill="none" stroke="var(--rule)" stroke-width="2" stroke-dasharray="6 6"/>
  </svg>
  <div class="crowd crowd-small" role="img" aria-label="Illustration: audience silhouettes"></div>
  <div class="feather" role="img" aria-label="Illustration: white quill feather"></div>
  <div class="actors" role="img" aria-label="Illustration: three actors performing"></div>

  <h2 class="display h-components">The audience, the actors, and the story – <span class="accent">all rolled into one.</span></h2>

  <p class="body-text book">Book into a unique Silver Lantern Theatrical experience today| – and maybe, just maybe, you might survive…..</p>

  <p class="display url">www.silverlantern-example.com.au/theatre/</p>
</main>
</body>
</html>
```